Financial Services Postcard Design

Lionel Budwig, CPA
Financial Services
Accounting/Tax/Consulting
Services include but not limited to
Financial Statements
Tax Returns
CFO/Controller services
Budgeting and Forecasting
Cash Management
Payroll / AP/ AR
Insurance Analysis
Cost Analysis
Special projects

I need a postcard design for my new financial service company to assist businesses in the Orange County area of southern California. I'm looking for a warm but bright look to represent CPA with many years of Management experience with manufacturing companies that can relate to business issues and provide solutions for small business.

```html
<!DOCTYPE html>
<html lang="en">
<head>
<meta charset="utf-8">
<title>Lionel Budwig CPA – Financial Services Postcard</title>
<link rel="stylesheet" href="https://fonts.googleapis.com/css2?family=Cabin:wght@400;500&family=Marcellus+SC&display=swap">
<style>
  :root {
    --bg-light: #fdfaf6;
    --bg-mid: #ead8c4;
    --bg-dark: #d2a982;
    --frame-light: #e9dfd4;
    --frame-edge: #c9b6a4;
    --photo-warm: #d8cbb8;
    --photo-cool: #3a3a40;
    --panel-top: #ffffff;
    --panel-bottom: #ddd5cc;
    --ink: #1d1915;
    --name-brown: #7b5331;
  }
  * { margin: 0; padding: 0; box-sizing: border-box; }
  html, body { width: 1200px; height: 772px; overflow: hidden; }
  body { background: var(--bg-light); }

  .postcard {
    position: relative;
    width: 1200px;
    height: 772px;
    overflow: hidden;
    background: linear-gradient(90deg, var(--bg-light) 0%, var(--bg-mid) 45%, var(--bg-dark) 100%);
  }

  .portrait-frame {
    position: absolute;
    left: 40px;
    top: 41px;
    width: 434px;
    height: 634px;
    background: linear-gradient(135deg, var(--frame-edge), var(--frame-light) 30%, var(--frame-light) 70%, var(--frame-edge));
    box-shadow: inset 0 0 6px rgba(120, 90, 60, 0.35);
  }
  .portrait {
    position: absolute;
    left: 16px;
    top: 16px;
    width: 402px;
    height: 602px;
    background:
      radial-gradient(ellipse 60% 40% at 50% 80%, var(--photo-cool) 0%, rgba(58,58,64,0.9) 60%, transparent 61%),
      linear-gradient(180deg, var(--photo-warm) 0%, #cbbca6 100%);
    box-shadow: inset 0 0 40px rgba(90, 60, 40, 0.45);
  }

  .name-line {
    position: absolute;
    left: 110px;
    top: 678px;
    display: flex;
    align-items: baseline;
    gap: 18px;
  }
  .name {
    font-family: "Cabin", sans-serif;
    font-weight: 400;
    font-size: 42px;
    color: var(--name-brown);
  }
  .credential {
    font-family: "Cabin", sans-serif;
    font-size: 20px;
    color: var(--ink);
  }

  .headline-panel {
    position: absolute;
    left: 553px;
    top: 45px;
    width: 557px;
    height: 137px;
    border-radius: 22px;
    background: linear-gradient(180deg, var(--panel-top) 0%, #f3efea 40%, var(--panel-bottom) 100%);
    display: flex;
    flex-direction: column;
    justify-content: center;
    align-items: center;
  }
  .headline {
    font-family: "Marcellus SC", serif;
    font-weight: 400;
    font-size: 34px;
    line-height: 56px;
    color: var(--ink);
    text-align: center;
    letter-spacing: 0.5px;
  }

  .service-list {
    position: absolute;
    left: 553px;
    top: 222px;
    width: 557px;
    list-style: none;
    text-align: center;
    font-family: "Marcellus SC", serif;
    font-size: 25px;
    line-height: 42.4px;
    color: var(--ink);
  }
</style>
</head>
<body>
  <main class="postcard">
    <div class="portrait-frame">
      <div class="portrait" role="img" aria-label="Portrait photograph of Lionel Budwig in a dark suit and plaid tie"></div>
    </div>

    <div class="name-line">
      <span class="name">Lionel Budwig</span>
      <span class="credential">CPA</span>
    </div>

    <header class="headline-panel">
      <h1 class="headline">I Have Many Years of Experience<br>to Offer these Services to You</h1>
    </header>

    <ul class="service-list">
      <li>Financial Services</li>
      <li>Accounting/Tax/Consulting</li>
      <li>Services include but not limited to</li>
      <li>Financial Statements</li>
      <li>Tax Returns</li>
      <li>CFO/Controller services</li>
      <li>Budgeting and Forecasting</li>
      <li>Cash Management</li>
      <li>Payroll / AP/ AR</li>
      <li>Insurance Analysis</li>
      <li>Cost Analysis</li>
      <li>Special projects</li>
    </ul>
  </main>
</body>
</html>
```